Letterhead & Powerpoint Template Design for a Commercial Solar Company

We need these designs for a growing commercial solar company in Austin Texas. We specialize in large-scale/commercial installations. Any assets we design should have the following elements/considerations.
-Authoritative
-Crisp
-Professional
-No Cartoonish Graphics / nothing "cute"
-Should feel more like an engineering firm style than what you typically solar companies
-Not overwhelming

Ultimately are looking for the following in this design
-Letterhead design
-Powerpoint Design (horizontal Pitch deck with a title page design template 3-4 different layouts that we can alternate or use as needed)
-Proposal Design (Vertical layout that has a very professional title page and then just a standard template for interior pages)
-Business Card

Preferred fonts are Inter & Roboto

Dropbox of photo assets to use - https://www.filevaultor.net/sh/pwmtrebxnhqz4ka/KKRfe527ytbwQmZdHrVnPo8Zc?dl=0

Target Market(s)

C-Suites, Decision Makers, Commercial property owners

Industry/Entity Type

Solar

Font styles to use
Other font styles liked:
• Inter (Primary) Roboto (Secondary)

Colors

Designer to choose colors to be used in the design.

Requirements
Must have
• Authoritative Crisp Styling
Should not have
• cartoonish or bubbly graphics.

```html
<!DOCTYPE html>
<html lang="en">
<head>
<meta charset="utf-8">
<title>Meridian Grid – Stationery &amp; Proposal</title>
<link href="https://fonts.googleapis.com/css2?family=Inter:wght@400;500;600&family=Roboto:wght@300;400;500;700;900&family=Rubik:wght@600;700&display=swap" rel="stylesheet">
<style>
:root{
  --orange:#f15a29;
  --ink:#3d3d3f;
  --grey:#6d6e71;
  --light:#c9cacc;
  --board:#e3e4e6;
  --paper:#ffffff;
}
*{margin:0;padding:0;box-sizing:border-box}
html,body{width:1200px;height:556px;overflow:hidden;background:var(--board);font-family:'Roboto',sans-serif;color:var(--grey)}
.board{position:relative;width:1200px;height:556px}
.abs{position:absolute}
.piece-label{position:absolute;font-family:'Inter',sans-serif;font-size:9.5px;color:#5a5b5e;font-weight:400}
.sheet{position:absolute;background:var(--paper);box-shadow:1px 2px 4px rgba(0,0,0,.18);overflow:hidden}

/* brand name lockup */
.brand{position:absolute;display:flex;align-items:center;gap:4px;font-family:'Inter',sans-serif;font-weight:500;color:var(--ink);letter-spacing:.08em;text-transform:uppercase;white-space:nowrap}
.brand .mark{display:block;background:var(--orange)}
.brand.on-orange{color:#fff}
.brand.on-orange .mark{background:#fff}

/* contact rows */
.contact{position:absolute;font-size:5px;color:var(--grey);line-height:1}
.contact .row{display:flex;align-items:center;gap:3px;height:9.6px}
.contact.right .row{justify-content:flex-end}
.ico{width:5px;height:5px;background:var(--orange);border-radius:.6px;display:inline-block;position:relative}
.ico svg{position:absolute;inset:0}

/* footer band */
.foot-band{position:absolute;left:0;height:6px;background:var(--orange);color:#fff;font-size:4.4px;display:flex;align-items:center;padding-left:18px;clip-path:polygon(0 0,92% 0,100% 100%,0 100%)}
.foot-line{position:absolute;height:1px;background:var(--ink)}

/* business card */
.card-name{font-size:7.4px;font-weight:700;color:var(--ink)}
.card-name span{color:var(--orange)}
.card-title{font-size:5.4px;color:var(--grey)}

/* letterhead */
.lh-name{font-family:'Inter',sans-serif;font-size:10px;color:var(--orange);letter-spacing:.02em}
.lh-info{font-size:5.6px;color:var(--grey);line-height:1.3}
.lh-body{position:absolute;left:18px;width:278px;font-size:5.8px;line-height:8.3px;color:#8a8b8e;text-align:justify;font-weight:300}
.lh-body p{margin-bottom:8px}
.lh-body p.gap{margin-bottom:16px}

/* proposal */
.headline{position:absolute;text-align:right;font-family:'Rubik',sans-serif;line-height:1}
.headline .h1{color:var(--orange);font-weight:700}
.headline .h2{color:var(--ink);font-weight:700;padding-bottom:2px;border-bottom:1px solid var(--ink)}
.headline .h3{color:var(--ink);font-weight:600;margin-top:3px}
.cover-title{position:absolute;color:#fff;font-family:'Roboto',sans-serif;line-height:1}
.bullets{position:absolute;right:12px;text-align:right;font-size:6.4px;color:var(--ink);line-height:10.6px}
.site{position:absolute;font-size:7.4px;letter-spacing:.17em;color:var(--ink)}
.site span{color:var(--orange)}
</style>
</head>
<body>
<main class="board">

  <!-- Business card -->
  <div class="piece-label" style="left:31px;top:104px">Business Card</div>

  <section class="sheet business-card-front" style="left:31px;top:119px;width:211px;height:127px">
    <div class="brand" style="left:20px;top:57px;font-size:9px"><i class="mark" style="width:6px;height:6px"></i>Meridian Grid</div>
    <div class="abs" style="left:110px;top:18px;width:1px;height:70px;background:linear-gradient(#fff,#e4e4e4,#fff)"></div>
    <div class="abs" style="left:119px;top:32px">
      <div class="card-name">DANA. <span>WHITFIELD</span></div>
      <div class="card-title" style="margin-top:2px">Managing Director</div>
      <div class="abs" style="left:0;top:18px;width:22px;height:1px;background:var(--orange)"></div>
    </div>
    <div class="contact" style="left:119px;top:55px">
      <div class="row"><i class="ico"></i>+00 123 456 78</div>
      <div class="row"><i class="ico"></i>hello@meridiangrid.co</div>
      <div class="row"><i class="ico"></i>www.companywebsite.com</div>
    </div>
    <div class="foot-band" style="top:106px;width:142px">5180 Ridgeline Blvd, Cedar Park, TX 78613</div>
    <div class="foot-line" style="top:108px;left:138px;right:0"></div>
  </section>

  <section class="sheet business-card-back" style="left:30px;top:271px;width:211px;height:127px;background:var(--orange)">
    <div class="brand on-orange" style="left:54px;top:56px;font-size:12px"><i class="mark" style="width:8px;height:8px"></i>Meridian Grid</div>
  </section>

  <!-- Letterhead -->
  <div class="piece-label" style="left:266px;top:24px">Letterhead</div>

  <section class="sheet letterhead" style="left:263px;top:41px;width:308px;height:436px">
    <div class="brand" style="left:18px;top:33px;font-size:9px"><i class="mark" style="width:6px;height:6px"></i>Meridian Grid</div>
    <div class="contact right" style="right:12px;top:16px">
      <div class="row">+00 123 456 78 <i class="ico"></i></div>
      <div class="row">hello@meridiangrid.co <i class="ico"></i></div>
      <div class="row">www.companywebsite.com <i class="ico"></i></div>
    </div>

    <div class="lh-name abs" style="left:18px;top:98px">MARLA ORTEGA</div>
    <div class="lh-info abs" style="left:18px;top:115px">0123-456-789</div>
    <div class="lh-info abs" style="left:18px;top:125px">info@northlineoffice.com</div>
    <div class="lh-info abs" style="left:18px;top:135px;line-height:7px">2210 Harlow St. Suite<br>140 Austin, TX 78701</div>
    <div class="lh-info abs" style="right:14px;top:140px;font-size:6.2px;color:var(--ink)">12 December, 2023</div>

    <div class="lh-body" style="top:159px">
      <p>Lorem ipsum dolor sit amet, consectetuer adipiscing elit, sed diam nonummy nibh euismod tincidunt ut laoreet dolore magna aliquam erat volutpat. Ut wisi enim ad minim veniam, quis nostrud exerci tation ullamcorper suscipit lobortis nisl ut aliquip ex ea commodo consequat. Duis autem vel eum iriure dolor in hendrerit in vulputate velit esse molestie consequat, vel illum dolore eu feugiat nulla facilisis at vero eros et accumsan et iusto odio dignissim qui blandit praesent luptatum zzril delenit augue duis dolore te feugait nulla facilisi.</p>
      <p class="gap">Lorem ipsum dolor sit amet, cons ectetuer adipiscing elit, sed diam nonummy nibh euismod tincidunt ut laoreet dolore magna aliquam erat volutpat. Ut wisi enim ad minim veniam, quis nostrud exerci tation ullamcorper suscipit lobortis nisl ut aliquip ex ea commodo consequat. Lorem ipsum dolor sit amet, consectetuer adipiscing elit, sed diam nonummy nibh euismod tincidunt ut laoreet dolore magna aliquam erat</p>
      <p>Lorem ipsum dolor sit amet, cons ectetuer adipiscing elit, sed diam nonummy nibh euismod tincidunt ut laoreet dolore magna aliquam erat volutpat. Ut wisi enim ad minim veniam, quis nostrud exerci tation ullamcorper suscipit lobortis nisl ut aliquip ex ea commodo consequat. Lorem ipsum dolor sit zamet, consectetuer adipiscing elit, sed diam nonummy nibh euismod tincidunt.</p>
    </div>

    <div class="abs" style="left:226px;top:340px;font-size:7px;color:var(--grey)">Managing Director</div>
    <div class="abs" role="img" aria-label="Handwritten signature" style="left:232px;top:352px;width:52px;height:30px;background:linear-gradient(90deg,rgba(0,0,0,0),rgba(40,40,40,.12),rgba(0,0,0,0));border-radius:4px"></div>

    <div class="foot-band" style="top:413px;width:160px">5180 Ridgeline Blvd, Cedar Park, TX 78613</div>
    <div class="foot-line" style="top:417px;left:155px;right:0"></div>
  </section>

  <!-- Proposal -->
  <div class="piece-label" style="left:595px;top:86px">Proposal Design</div>

  <section class="sheet proposal-cover" style="left:595px;top:110px;width:283px;height:366px">
    <div class="brand" style="left:16px;top:38px;font-size:10px"><i class="mark" style="width:7px;height:7px"></i>Meridian Grid</div>

    <div class="headline" style="right:20px;top:14px">
      <div class="h1" style="font-size:12.5px">Headeline</div>
      <div class="h2" style="font-size:13.5px;margin-top:1px">Lorem Ipsum</div>
      <div class="h3" style="font-size:6.6px">Space Here</div>
    </div>

    <svg class="abs" style="left:0;top:0" width="283" height="366" viewBox="0 0 283 366">
      <rect x="218" y="62" width="80" height="80" rx="10" fill="#c8c9cb"/>
      <g role="img" aria-label="Photo of a solar installer in hard hat and safety vest working on a rooftop array">
        <defs>
          <linearGradient id="photoTone" x1="0" y1="0" x2="1" y2="1">
            <stop offset="0" stop-color="#6f7a84"/>
            <stop offset=".55" stop-color="#9aa3a8"/>
            <stop offset="1" stop-color="#c6b24a"/>
          </linearGradient>
        </defs>
        <path d="M86 77 H258 Q269 77 265 88 L224 256 Q219 266 208 266 H40 L76 86 Q78 77 86 77 Z" fill="url(#photoTone)"/>
      </g>
      <path d="M0 164 H192 L164 311 Q161 321 150 321 H0 Z" fill="var(--orange)" opacity=".95"/>
      <path d="M72 122 H239 L186 288 Q182 293 176 293 H160" fill="none" stroke="var(--orange)" stroke-width="1.2"/>
      <path d="M72 122 Q64 122 62 132 L52 164" fill="none" stroke="var(--orange)" stroke-width="1.2"/>
    </svg>

    <div class="cover-title" style="left:19px;top:197px;font-size:27px;font-weight:400">ANNUAL</div>
    <div class="cover-title" style="left:18px;top:225px;font-size:34px;font-weight:900">REPORT</div>
    <div class="abs" style="left:20px;top:253px;width:56px;height:2.5px;background:#fff"></div>
    <div class="cover-title" style="left:21px;top:262px;font-size:44px;font-weight:400">2023</div>

    <div class="abs" style="right:13px;top:292px;font-family:'Roboto',sans-serif;font-weight:700;font-size:12px;color:var(--orange)">LOREM IPSUM</div>
    <div class="bullets" style="top:311px">
      Lorem ipsum dolor •<br>sit amet, consectetuer •<br>adipiscing elit, sed diam •
    </div>
    <div class="site" style="left:17px;top:334px">www.<span>companywebsite</span>.com</div>
  </section>

  <section class="sheet proposal-interior" style="left:899px;top:110px;width:283px;height:366px">
    <div class="brand" style="left:12px;top:24px;font-size:7.5px"><i class="mark" style="width:5px;height:5px"></i>Meridian Grid</div>
    <div class="headline" style="right:19px;top:13px">
      <div class="h1" style="font-size:11px">Headeline</div>
      <div class="h2" style="font-size:11px;margin-top:1px">Lorem Ipsum</div>
      <div class="h3" style="font-size:5px">Space Here</div>
    </div>
    <div class="abs" style="left:0;top:348px;width:260px;height:1.5px;background:linear-gradient(90deg,rgba(241,90,41,.25),var(--orange))"></div>
    <div class="abs" style="left:261px;top:344px;font-size:5.5px;font-weight:700;color:var(--ink)">02</div>
    <div class="abs" style="left:271px;top:348px;width:12px;height:1.5px;background:var(--orange)"></div>
  </section>

</main>
</body>
</html>
```